Safety Training company business card design

We are after a high quality, professional business card. We are open to a single or double sided card.

The winning designer must provide the card in a format where we can easily change the name and details of the different people in our organization.

Harbor Guard's company colour is lime green.

We provide all aspects of safety advisory and training for the Building, Civil Construction, Mining, Oil and Gas, Manufacturing, Rail, Rural and Retail sectors.

Visit our website www.harborguard.com.au for training competencies we offer along with our other services including RPL's, safety audits, professional development and client support.

Target Market(s)

Those in the Building, Civil Construction, Mining, Oil and Gas, Manufacturing, Rail, Rural and Retail industries.

Industry/Entity Type

Training

Contact Information for Business Card

Harbor Guard
Safety and Training
Dennis Palworth
Director
M 0427 518 266
dennis@harborguard.com.au
www.harborguard.com.au
(2 business addresses:)
Corvin High Risk Training Centre
17 Tandem Parade, Kestrel Q 4219 P 3912 5486 F 3912 5174
Brenlow Training Centre
86 Fenwick Street, Calder Q 4752 P 4873 2615 F 4873 2249

Colors
9bcb3c

Requirements
Must have
• Lime green must be the main colour. must include HG logo attached, and state Harbor Guard (Safety and Training in smaller/different font).

State something along the lines of:

Nice to have
• We offer remote training and we can come to you.

```html
<!DOCTYPE html>
<html lang="en">
<head>
<meta charset="utf-8">
<title>Harbor Guard – Business Card Set</title>
<link rel="stylesheet" href="https://fonts.googleapis.com/css2?family=Open+Sans:wght@400;600;700;800&display=swap">
<style>
  :root{
    --lime:#9dcc3c;
    --lime-deep:#84b333;
    --red:#c8352b;
    --ink:#1c1c1c;
    --white:#ffffff;
    --stage-light:#d4d4d4;
    --stage-dark:#3a3a3a;
  }
  *{margin:0;padding:0;box-sizing:border-box}
  html,body{width:1200px;height:900px;overflow:hidden}
  body{
    position:relative;
    font-family:"Open Sans",Arial,sans-serif;
    color:var(--ink);
    background:radial-gradient(ellipse at 30% 20%,var(--stage-light) 0%,#9a9a9a 55%,var(--stage-dark) 100%);
  }
  .card{
    position:absolute;
    height:330px;
    overflow:hidden;
    box-shadow:0 2px 6px rgba(0,0,0,.45);
    background:var(--lime);
  }
  .card-front{left:42px;width:550px}
  .card-back{left:614px;width:552px}
  .row-top{top:84px}
  .row-bottom{top:455px}
  .card-art{position:absolute;inset:0;width:100%;height:100%}

  .brand{
    position:absolute;
    font-weight:800;
    letter-spacing:1px;
    line-height:1;
    white-space:nowrap;
  }
  .tagline{
    position:absolute;
    font-size:14px;
    letter-spacing:3.6px;
    color:var(--white);
    white-space:nowrap;
  }
  .card-front .brand{left:68px;top:44px;font-size:34px;color:var(--red)}
  .card-front .tagline{left:134px;top:86px}

  .person{position:absolute;left:26px;top:186px}
  .person-name{font-size:20px;font-weight:600;color:var(--red);line-height:1.1}
  .person-role{font-size:13px;margin-top:3px}
  .contact{list-style:none;position:absolute;left:26px;top:236px;font-size:13px}
  .contact li{display:flex;align-items:center;height:20px}
  .icon{width:11px;height:11px;margin-right:10px;flex:none}
  .strapline{
    position:absolute;left:0;right:0;top:303px;height:24px;
    background:var(--red);color:var(--white);
    font-size:14px;text-align:center;line-height:24px;
  }

  .card-back .brand{left:182px;top:50px;font-size:36px;color:var(--white)}
  .card-back .tagline{left:216px;top:89px}
  .services{
    position:absolute;left:166px;width:350px;top:121px;
    font-size:13px;line-height:19.5px;text-align:center;
  }
  .centre{position:absolute;top:242px;font-size:13px;line-height:19.5px}
  .centre-one{left:31px}
  .centre-two{left:300px}
  .centre-name{color:var(--red);font-weight:700}
  .centre p{display:flex;align-items:center}
</style>
</head>
<body>

<!-- Front, top -->
<section class="card card-front row-top">
  <svg class="card-art" viewBox="0 0 550 330" aria-hidden="true">
    <path d="M0,136 C140,178 330,176 550,108 L550,330 L0,330Z" fill="var(--lime-deep)"/>
    <path d="M108,164 C300,176 470,122 550,48 L550,70 C470,146 300,186 108,164Z" fill="var(--red)"/>
  </svg>
  <div class="brand">HARBOR GUARD</div>
  <div class="tagline">SAFETY AND TRAINING</div>
  <div class="person">
    <div class="person-name">DENNIS PALWORTH</div>
    <div class="person-role">Director</div>
  </div>
  <ul class="contact">
    <li><svg class="icon" viewBox="0 0 11 11"><rect width="11" height="11" rx="2" fill="var(--red)"/><rect x="3.5" y="2" width="4" height="7" rx=".8" fill="var(--white)"/></svg>0427 518 266</li>
    <li><svg class="icon" viewBox="0 0 11 11"><rect width="11" height="11" rx="2" fill="var(--red)"/><rect x="2" y="3" width="7" height="5" fill="var(--white)"/><path d="M2,3 L5.5,6 L9,3" stroke="var(--red)" fill="none"/></svg>dennis@harborguard.com.au</li>
    <li><svg class="icon" viewBox="0 0 11 11"><rect width="11" height="11" rx="2" fill="var(--red)"/><circle cx="5.5" cy="5.5" r="3.3" stroke="var(--white)" fill="none"/><path d="M2.2,5.5 H8.8 M5.5,2.2 V8.8" stroke="var(--white)"/></svg>www.harborguard.com.au</li>
  </ul>
  <div class="strapline">We offer remote training and we can come to you</div>
</section>

<!-- Back, top -->
<section class="card card-back row-top">
  <svg class="card-art" viewBox="0 0 552 330" aria-hidden="true">
    <path d="M0,0 L76,0 C-10,100 80,222 492,232 L552,212 L552,330 L0,330Z" fill="var(--lime-deep)"/>
    <path d="M76,0 C-10,100 80,222 492,232 C120,212 40,112 112,0Z" fill="var(--red)"/>
  </svg>
  <div class="brand">HARBOR GUARD</div>
  <div class="tagline">SAFETY AND TRAINING</div>
  <p class="services">We provide all aspects of safety advisory and training for the Building, Civil Construction, Mining, Oil and Gas, Manufacturing, Rail, Rural and Retail sectors.</p>
  <div class="centre centre-one">
    <div class="centre-name">Corvin High Risk Training Centre</div>
    <p>17 Tandem Parade, Kestrel Q 4219</p>
    <p><svg class="icon" viewBox="0 0 11 11"><rect width="11" height="11" rx="2" fill="var(--red)"/><path d="M3,2.5 L4.5,2.5 L5,4.5 L4,5.2 Q5,7 6,7.2 L6.8,6.2 L8.5,6.8 L8.5,8.5 Q4,8.5 3,2.5Z" fill="var(--white)"/></svg>07 3912 5486</p>
    <p><svg class="icon" viewBox="0 0 11 11"><rect width="11" height="11" rx="2" fill="var(--red)"/><rect x="2.5" y="4" width="6" height="4.5" fill="var(--white)"/><rect x="4" y="2" width="3" height="2" fill="var(--white)"/></svg>07 3912 5174</p>
  </div>
  <div class="centre centre-two">
    <div class="centre-name">Brenlow Training Centre</div>
    <p>86 Fenwick Street, Calder Q 4752</p>
    <p><svg class="icon" viewBox="0 0 11 11"><rect width="11" height="11" rx="2" fill="var(--red)"/><path d="M3,2.5 L4.5,2.5 L5,4.5 L4,5.2 Q5,7 6,7.2 L6.8,6.2 L8.5,6.8 L8.5,8.5 Q4,8.5 3,2.5Z" fill="var(--white)"/></svg>07 4873 2615</p>
    <p><svg class="icon" viewBox="0 0 11 11"><rect width="11" height="11" rx="2" fill="var(--red)"/><rect x="2.5" y="4" width="6" height="4.5" fill="var(--white)"/><rect x="4" y="2" width="3" height="2" fill="var(--white)"/></svg>07 4873 2249</p>
  </div>
</section>

<!-- Front, bottom -->
<section class="card card-front row-bottom">
  <svg class="card-art" viewBox="0 0 550 330" aria-hidden="true">
    <path d="M0,136 C140,178 330,176 550,108 L550,330 L0,330Z" fill="var(--lime-deep)"/>
    <path d="M108,164 C300,176 470,122 550,48 L550,70 C470,146 300,186 108,164Z" fill="var(--red)"/>
  </svg>
  <div class="brand">HARBOR GUARD</div>
  <div class="tagline">SAFETY AND TRAINING</div>
  <div class="person">
    <div class="person-name">DENNIS PALWORTH</div>
    <div class="person-role">Director</div>
  </div>
  <ul class="contact">
    <li><svg class="icon" viewBox="0 0 11 11"><rect width="11" height="11" rx="2" fill="var(--red)"/><rect x="3.5" y="2" width="4" height="7" rx=".8" fill="var(--white)"/></svg>0427 518 266</li>
    <li><svg class="icon" viewBox="0 0 11 11"><rect width="11" height="11" rx="2" fill="var(--red)"/><rect x="2" y="3" width="7" height="5" fill="var(--white)"/><path d="M2,3 L5.5,6 L9,3" stroke="var(--red)" fill="none"/></svg>dennis@harborguard.com.au</li>
    <li><svg class="icon" viewBox="0 0 11 11"><rect width="11" height="11" rx="2" fill="var(--red)"/><circle cx="5.5" cy="5.5" r="3.3" stroke="var(--white)" fill="none"/><path d="M2.2,5.5 H8.8 M5.5,2.2 V8.8" stroke="var(--white)"/></svg>www.harborguard.com.au</li>
  </ul>
  <div class="strapline">We offer remote training and we can come to you</div>
</section>

<!-- Back, bottom -->
<section class="card card-back row-bottom">
  <svg class="card-art" viewBox="0 0 552 330" aria-hidden="true">
    <path d="M0,0 L76,0 C-10,100 80,222 492,232 L552,212 L552,330 L0,330Z" fill="var(--lime-deep)"/>
    <path d="M76,0 C-10,100 80,222 492,232 C120,212 40,112 112,0Z" fill="var(--red)"/>
  </svg>
  <div class="brand">HARBOR GUARD</div>
  <div class="tagline">SAFETY AND TRAINING</div>
  <p class="services">We provide all aspects of safety advisory and training for the Building, Civil Construction, Mining, Oil and Gas, Manufacturing, Rail, Rural and Retail sectors.</p>
  <div class="centre centre-one">
    <div class="centre-name">Corvin High Risk Training Centre</div>
    <p>17 Tandem Parade, Kestrel Q 4219</p>
    <p><svg class="icon" viewBox="0 0 11 11"><rect width="11" height="11" rx="2" fill="var(--red)"/><path d="M3,2.5 L4.5,2.5 L5,4.5 L4,5.2 Q5,7 6,7.2 L6.8,6.2 L8.5,6.8 L8.5,8.5 Q4,8.5 3,2.5Z" fill="var(--white)"/></svg>07 3912 5486</p>
    <p><svg class="icon" viewBox="0 0 11 11"><rect width="11" height="11" rx="2" fill="var(--red)"/><rect x="2.5" y="4" width="6" height="4.5" fill="var(--white)"/><rect x="4" y="2" width="3" height="2" fill="var(--white)"/></svg>07 3912 5174</p>
  </div>
  <div class="centre centre-two">
    <div class="centre-name">Brenlow Training Centre</div>
    <p>86 Fenwick Street, Calder Q 4752</p>
    <p><svg class="icon" viewBox="0 0 11 11"><rect width="11" height="11" rx="2" fill="var(--red)"/><path d="M3,2.5 L4.5,2.5 L5,4.5 L4,5.2 Q5,7 6,7.2 L6.8,6.2 L8.5,6.8 L8.5,8.5 Q4,8.5 3,2.5Z" fill="var(--white)"/></svg>07 4873 2615</p>
    <p><svg class="icon" viewBox="0 0 11 11"><rect width="11" height="11" rx="2" fill="var(--red)"/><rect x="2.5" y="4" width="6" height="4.5" fill="var(--white)"/><rect x="4" y="2" width="3" height="2" fill="var(--white)"/></svg>07 4873 2249</p>
  </div>
</section>

</body>
</html>
```